Welding and farication business card

Business name Tmb Welding & Fabrication

I need a business card made for my welding and fabrication business that is bold and stands out. My business is both welding repairs on machinery and anything else you can imagine as well as fabricating new products. i have used this service before and was very happy with the out come of my design logo. i think the card should remain fairly simple and classy but also be bold. I think a black card would best be suited to the talk with my logo on it. i feel the back of the card should just have my logo and the front have my logo email, website and phone number and maybe incorporate a pagebook and snapgallery simple if it can be made look good these arnt a necessity.
I have included both my logo and some business card ideas below

Target Market(s)

Farmers, heavy industry, earthmoving, trucking

Industry/Entity Type

Engineering

Contact Information for Business Card

0438517264
dane@tmbweldingandfabrication.com.au
www.tmbweldingandfabrication.com.au

Colors
33a6d7
0255a3

Requirements
Must have
• Dane Whitlock
my phone number 0438517264
my logo
Preferably a black card desgn
Nice to have
• List of what i do,
Sheds and carports
Ute trays
Stockyards
Trailers
Farm equipment
Stockcrates
Gateways and Entrances
Breakdowns
Maintenance
And lots more!

```html
<!DOCTYPE html>
<html lang="en">
<head>
<meta charset="utf-8">
<title>Tmb Welding &amp; Fabrication – Business Card</title>
<link rel="stylesheet" href="https://fonts.googleapis.com/css2?family=Roboto+Condensed:wght@400;700&family=Archivo:wght@400;700&display=swap">
<style>
  :root {
    --page-bg: #e4e4e4;
    --card-white: #f4f4f4;
    --card-black: #121212;
    --brand-blue: #0255a3;
    --brand-sky: #33a6d7;
    --ink: #151515;
    --ink-soft: #2b2b2b;
    --white: #ffffff;
    --figure-tone: #2a2a2a;
  }
  * { box-sizing: border-box; margin: 0; padding: 0; }
  html, body {
    width: 1200px; height: 930px; overflow: hidden;
    background: var(--page-bg);
  }
  .sheet {
    width: 1200px; height: 930px;
    display: flex; align-items: center; justify-content: center; gap: 40px;
  }
  .card {
    position: relative;
    width: 540px; height: 330px;
    border-radius: 4px;
    overflow: hidden;
    box-shadow: 0 10px 26px rgba(0,0,0,0.14);
  }

  /* Front */
  .card--front { background: var(--card-white); }
  .contact-list {
    position: absolute; left: 36px; top: 32px;
    list-style: none;
    font-family: "Roboto Condensed", sans-serif;
    font-size: 15px; letter-spacing: 0.04em; text-transform: uppercase;
    color: var(--ink);
  }
  .contact-list li {
    display: flex; align-items: center; gap: 10px; height: 26px;
  }
  .contact-icon { width: 20px; height: 20px; flex: none; }
  .brand-name {
    font-family: "Archivo", sans-serif; font-weight: 700;
    text-transform: uppercase; line-height: 1.08;
  }
  .brand-name span { display: block; white-space: nowrap; }
  .brand-name--front {
    position: absolute; left: 36px; top: 122px;
    font-size: 26px;
    color: var(--brand-blue);
  }
  .owner-name {
    position: absolute; left: 36px; top: 188px;
    font-family: "Roboto Condensed", sans-serif; font-weight: 700;
    font-size: 15px; letter-spacing: 0.06em; text-transform: uppercase;
    color: var(--ink);
  }
  .social-list {
    position: absolute; left: 36px; top: 236px;
    list-style: none;
    font-family: "Roboto Condensed", sans-serif; font-size: 13px;
    color: var(--ink-soft);
  }
  .social-list li { display: flex; align-items: center; gap: 8px; height: 24px; }
  .social-dot {
    width: 16px; height: 16px; border-radius: 50%; background: var(--brand-blue);
  }
  .welder-figure {
    position: absolute; right: 0; bottom: 0;
    width: 230px; height: 190px;
    background: linear-gradient(135deg, #d9d9d9 0%, var(--figure-tone) 100%);
    border-top-left-radius: 120px;
  }

  /* Back */
  .card--back { background: var(--card-black); color: var(--white); }
  .service-list {
    position: absolute; left: 36px; top: 62px;
    list-style: none;
    font-family: "Archivo", sans-serif;
    font-size: 14px; letter-spacing: 0.03em; text-transform: uppercase;
    line-height: 27px;
  }
  .service-list li::before {
    content: ""; display: inline-block;
    width: 6px; height: 6px; border-radius: 50%;
    background: var(--brand-sky); margin-right: 8px; vertical-align: middle;
  }
  .brand-name--back {
    position: absolute; right: 30px; top: 136px;
    text-align: right;
    font-size: 24px;
    color: var(--white);
  }
</style>
</head>
<body>
<main class="sheet">

  <section class="card card--front" aria-label="Card front">
    <ul class="contact-list">
      <li>
        <svg class="contact-icon" viewBox="0 0 20 20" aria-hidden="true">
          <circle cx="10" cy="10" r="10" fill="var(--brand-blue)"/>
          <path d="M7 5.5l1.6 2.4-1 1.1c.6 1.3 1.5 2.2 2.8 2.8l1.1-1 2.4 1.6-.9 1.7c-3.6-.4-6.6-3.4-7-7z" fill="#fff"/>
        </svg>
        0438517264
      </li>
      <li>
        <svg class="contact-icon" viewBox="0 0 20 20" aria-hidden="true">
          <circle cx="10" cy="10" r="10" fill="var(--brand-blue)"/>
          <rect x="5" y="6.5" width="10" height="7" fill="none" stroke="#fff" stroke-width="1.2"/>
          <path d="M5 6.5l5 4 5-4" fill="none" stroke="#fff" stroke-width="1.2"/>
        </svg>
        dane@tmbweldingandfabrication.com.au
      </li>
      <li>
        <svg class="contact-icon" viewBox="0 0 20 20" aria-hidden="true">
          <circle cx="10" cy="10" r="10" fill="var(--brand-blue)"/>
          <circle cx="10" cy="10" r="5" fill="none" stroke="#fff" stroke-width="1.1"/>
          <ellipse cx="10" cy="10" rx="2.2" ry="5" fill="none" stroke="#fff" stroke-width="1.1"/>
          <path d="M5 10h10" stroke="#fff" stroke-width="1.1"/>
        </svg>
        www.tmbweldingandfabrication.com.au
      </li>
    </ul>

    <p class="brand-name brand-name--front"><span>Tmb Welding &amp;</span><span>Fabrication</span></p>
    <p class="owner-name">Dane Whitlock</p>

    <ul class="social-list">
      <li><span class="social-dot"></span>pagebook</li>
      <li><span class="social-dot"></span>snapgallery</li>
    </ul>

    <div class="welder-figure" role="img" aria-label="Black line illustration of a welder in a helmet working with a torch and sparks"></div>
  </section>

  <section class="card card--back" aria-label="Card back">
    <ul class="service-list">
      <li>Sheds</li>
      <li>Ute trays</li>
      <li>Cattle and sheep yards</li>
      <li>Trailers</li>
      <li>Farm equipment</li>
      <li>Gateways and entrances</li>
      <li>And lots more!</li>
    </ul>
    <p class="brand-name brand-name--back"><span>Tmb Welding &amp;</span><span>Fabrication</span></p>
  </section>

</main>
</body>
</html>
```